Mortgage and Asset Finance Broker Needs a Wordpress Website Design

I need a modern looking Wordpress website to showcase my service as a mortgage and asset broker. I have a company and we work with various lenders to arrange mortgages, as well as commercial lending and business asset finance. The website needs to look professional, be easy to navigate and capture leads. SEO is obviously very important to me. It really needs to be something that shows trust and professioanlism.
Updates

On the home page I will need to have some boxes for Home Loans, Refinancing, Business (and Agriculture) Loans etc. I'd like a carousel in the middle which shows our lenders (so that can have the banks logos added).

It needs to be easy top navigate and showcase all we do - Home Loans, Refinancing, Commercial Loans, Car Loans, Asset Finance etc.

There are plenty of companies on the internet that do this.

There is some good information here https://lendtrellis.com.au/mortgage-broker-homepage/

I need to make sure that editing the website is easy (I think Wordpress has something that allows that).

Also we are very much an Australian business so that is something to advertise.

Industry/Entity Type

Mortgage and Finance Broker

Coding

Coded - Design and coding required

Number of Pages Required

5+ page

Requirements
Must have
• Easy to navigate professional feel. Must be responsive and mobile friendly.
Nice to have
• Homepage with links to inner pages. Contact buttons.

```html
<!DOCTYPE html>
<html lang="en">
<head>
<meta charset="utf-8">
<title>Kestrel Financial Services – Home</title>
<link href="https://fonts.googleapis.com/css2?family=Inter:wght@300;400;500;600;700&display=swap" rel="stylesheet">
<style>
:root{
  --canvas:#f1f1f2;
  --navy:#0b1a3b;
  --navy-2:#0f2350;
  --blue:#1a5fb4;
  --blue-bright:#2a63d4;
  --hero-a:#173a9c;
  --hero-b:#2e5ad0;
  --ink:#1b2236;
  --muted:#6b7385;
  --light:#cfdcf5;
  --white:#ffffff;
  --line:#d9dee8;
}
*{box-sizing:border-box;margin:0;padding:0}
html,body{width:1200px;height:1200px;overflow:hidden}
body{background:var(--canvas);font-family:"Inter",sans-serif;color:var(--ink);position:relative}
.page{position:absolute;left:440px;top:0;width:1280px;height:4820px;transform:scale(.2489);transform-origin:0 0;background:var(--white);overflow:hidden}
.abs{position:absolute}
.label{font-size:11px;font-weight:600;letter-spacing:.04em;text-transform:uppercase;color:var(--blue-bright);display:flex;align-items:center;gap:14px}
.label::before{content:"";width:92px;height:1px;background:currentColor;opacity:.6}
.h2{font-size:40px;font-weight:300;line-height:1.12}
.body-text{font-size:11px;line-height:1.65;color:var(--muted)}
.btn{display:inline-flex;align-items:center;height:36px;border-radius:6px;overflow:hidden;font-size:12px;font-weight:500}
.btn span{padding:0 20px;line-height:32px;border:2px solid var(--navy);border-right:none;border-radius:6px 0 0 6px;background:var(--white);color:var(--navy)}
.btn i{width:30px;height:36px;background:var(--navy);display:flex;align-items:center;justify-content:center}
.btn.light span{border-color:var(--white)}
.btn.light i{background:var(--white)}
.brand{font-weight:700;color:var(--white);letter-spacing:-.02em}

/* hero */
.hero{left:0;top:0;width:1280px;height:664px;background:linear-gradient(120deg,var(--hero-a),var(--hero-b) 60%,#2447b5)}
.hero-photo{right:0;top:0;width:560px;height:664px;
  background:
    radial-gradient(ellipse 45% 55% at 55% 55%,rgba(214,196,168,.55),rgba(214,196,168,0) 70%),
    linear-gradient(90deg,rgba(46,90,208,1) 0%,rgba(46,90,208,0) 30%),
    linear-gradient(180deg,#2f56c4 0%,#1e3a92 55%,#142b6e 100%)}
.nav{left:80px;top:18px;right:66px;height:44px;display:flex;align-items:center}
.nav .brand{font-size:34px}
.nav ul{list-style:none;display:flex;gap:26px;margin-left:210px;font-size:11px;color:var(--light)}
.nav ul li:first-child{color:var(--white);font-weight:600}
.nav .cta{margin-left:auto;border:1.5px solid var(--white);border-radius:6px;color:var(--white);font-size:12px;padding:9px 18px}
.hero h1{left:67px;top:130px;font-size:52px;font-weight:300;line-height:1.15;color:var(--white)}
.hero h1 b{font-weight:700}
.hero .lead{left:67px;top:325px;width:320px;font-size:11px;line-height:1.6;color:var(--light)}
.hero .btn{left:67px;top:398px}
.service-tiles{left:67px;top:488px;display:flex;gap:12px}
.tile{width:218px;height:147px;border-radius:10px;background:rgba(255,255,255,.16);border:1px solid rgba(255,255,255,.3);padding:20px 18px;color:var(--white)}
.tile svg{display:block;margin-bottom:10px}
.tile h3{font-size:15px;font-weight:400;margin-bottom:10px}
.tile p{font-size:9px;line-height:1.6;color:var(--light)}

/* about */
.about-label{left:0;width:1280px;top:740px;justify-content:center}
.about h2{left:0;width:1280px;top:780px;text-align:center}
.about-copy{left:165px;top:950px;width:395px}
.about-copy p{margin-bottom:14px}
.bullets{display:grid;grid-template-columns:1fr 1fr;gap:18px 10px;margin-top:12px;font-size:10px;color:var(--muted)}
.bullets li{list-style:none;display:flex;align-items:center;gap:6px}
.bullets li::before{content:"";width:8px;height:8px;border-radius:50%;background:var(--blue-bright)}
.about .btn{left:165px;top:1178px}
.about-photo{left:648px;top:925px;width:448px;height:345px;border-radius:6px;background:linear-gradient(180deg,#dfe5ee,#a7b0bf 55%,#eef0f3);box-shadow:0 10px 30px rgba(0,0,0,.12)}
.about-photo-small{left:1048px;top:1070px;width:170px;height:225px;border:6px solid var(--white);border-radius:6px;background:linear-gradient(160deg,#c9d2e0,#8e9bb2);box-shadow:0 10px 30px rgba(0,0,0,.18)}

/* services */
.services{left:0;top:1430px;width:1280px;height:766px;background:var(--navy)}
.services .label{left:67px;top:65px;color:var(--white)}
.services h2{left:67px;top:88px;color:var(--white)}
.services .intro{left:826px;top:110px;width:375px;color:#b9c3d8}
.svc-cards{left:67px;top:230px;display:flex;gap:16px}
.svc{width:372px;height:395px;border-radius:8px;border:1px solid #4e79c9;position:relative;overflow:hidden}
.svc .img{position:absolute;inset:0}
.svc .txt{position:absolute;left:26px;right:26px;bottom:30px;color:var(--white)}
.svc h3{font-size:24px;font-weight:300;line-height:1.1;margin-bottom:14px}
.svc p{font-size:9.5px;line-height:1.6;color:#dbe5f7}
.svc .btn{margin-top:18px;height:30px}
.svc .btn span{line-height:26px;font-size:11px;border-color:var(--white)}
.svc .btn i{height:30px}
.progress{left:67px;top:680px;width:1150px;display:flex;align-items:center;gap:14px;color:var(--white);font-size:11px}
.progress .bar{flex:1;height:1px;background:#3c4c70;margin-right:30px}
.circle{width:40px;height:40px;border-radius:50%;display:flex;align-items:center;justify-content:center}

/* why */
.why .label{left:67px;top:2350px}
.why h2{left:67px;top:2378px}
.why .body-text{left:67px;top:2525px;width:320px}
.why .btn{left:67px;top:2605px}
.why-photo{left:745px;top:2345px;width:473px;height:285px;border-radius:6px;background:linear-gradient(150deg,#eef1f5,#aeb6c3 60%,#4c5a76);box-shadow:0 10px 30px rgba(0,0,0,.15)}
.donut{left:610px;top:2452px}
.stat-note{font-size:10px;color:var(--ink);line-height:1.3}
.stat-note b{display:block;font-size:22px;font-weight:400;color:var(--blue)}

/* reviews */
.reviews{left:0;top:2864px;width:1280px;height:609px;background:var(--blue)}
.reviews .label{left:67px;top:78px;color:var(--white)}
.reviews h2{left:67px;top:106px;color:var(--white)}
.stars{left:67px;top:222px;color:var(--white);font-size:20px;letter-spacing:3px}
.quote{left:67px;top:252px;width:560px;font-size:26px;line-height:1.45;color:var(--white)}
.reviewer{left:67px;top:465px;display:flex;align-items:center;gap:14px;color:var(--white)}
.avatar{width:50px;height:50px;border-radius:50%;background:#c9cdd6}
.reviewer b{font-size:16px;font-weight:600;display:block}
.reviewer small{font-size:10px}
.reviews .mark{left:445px;top:472px;font-size:30px}
.reviews .divider{left:745px;top:210px;width:1px;height:275px;background:rgba(255,255,255,.4)}
.stats{left:840px;top:218px;display:grid;grid-template-columns:178px 178px;row-gap:46px;color:var(--white)}
.stats b{font-size:40px;font-weight:400;display:block;line-height:1}
.stats h4{font-size:9px;font-weight:700;margin:8px 0 6px;line-height:1.3}
.stats p{font-size:8px;line-height:1.5;color:#dbe5f7}

/* contact */
.contact .label{left:67px;top:3640px}
.contact h2{left:67px;top:3665px}
.contact .body-text{left:67px;top:3770px;width:260px}
.c-item{display:flex;align-items:center;gap:12px;font-size:10px}
.c-item .circle{width:40px;height:40px;background:var(--blue)}
.c-item b{font-weight:600;display:block}
.c-item span{color:var(--muted)}
.form-card{left:650px;top:3593px;width:486px;height:492px;background:var(--white);border-radius:10px;box-shadow:0 10px 40px rgba(20,40,90,.12);padding:38px 44px}
.form-card h3{font-size:38px;font-weight:300;margin-bottom:28px}
.field{border:1px solid var(--line);border-radius:4px;height:42px;font-size:10px;color:var(--muted);padding:14px 18px;margin-bottom:14px}
.row{display:flex;gap:6px}.row .field{flex:1}
.field.tall{height:98px}
.send{display:flex;height:38px;border:2px solid var(--blue);border-radius:6px;overflow:hidden;margin-top:4px;font-size:12px;font-weight:500}
.send span{flex:1;text-align:center;line-height:34px;color:var(--navy)}
.send i{width:32px;background:var(--blue);display:flex;align-items:center;justify-content:center}
.form-card small{display:block;text-align:center;font-size:8px;color:var(--muted);margin-top:14px;line-height:1.6}

/* cta + footer */
.footer{left:0;top:4367px;width:1280px;height:453px;background:var(--navy)}
.cta-card{left:162px;top:4192px;width:966px;height:284px;border-radius:10px;border:4px solid var(--white);background:linear-gradient(120deg,#1d49b4,#2b5cd0 55%,#2249aa);box-shadow:0 10px 30px rgba(0,0,0,.15)}
.cta-card .label{position:absolute;left:78px;top:48px;color:var(--white)}
.cta-card h2{position:absolute;left:78px;top:76px;color:var(--white);font-size:38px}
.cta-card p{position:absolute;left:662px;top:94px;width:250px;font-size:10px;line-height:1.6;color:#dbe5f7}
.cta-card .btn{position:absolute;left:662px;top:140px}
.f-brand{left:67px;top:4540px;font-size:58px}
.f-about{left:67px;top:4620px;width:240px;color:#b9c3d8;font-size:10px;line-height:1.6}
.socials{left:67px;top:4690px;display:flex;gap:12px}
.socials i{width:30px;height:30px;border-radius:50%;background:var(--blue-bright);display:block}
.f-col{top:4548px;color:var(--white)}
.f-col h4{font-size:24px;font-weight:400;margin-bottom:14px}
.f-col li{list-style:none;font-size:10px;line-height:2.7;color:#c6cfe0}
.f-bottom{left:67px;top:4780px;width:1150px;border-top:1px solid #2b3a5e;padding-top:16px;display:flex;justify-content:space-between;font-size:10px;color:#c6cfe0}
</style>
</head>
<body>
<div class="page">

  <!-- Hero -->
  <section class="hero abs">
    <div class="hero-photo abs" role="img" aria-label="Smiling businessman in a beige suit using his phone against a blue city skyline"></div>
    <nav class="nav abs">
      <span class="brand">kestrel</span>
      <ul><li>Home</li><li>About Us</li><li>Services</li><li>Why Us</li><li>Reviews</li><li>Contact Us</li></ul>
      <span class="cta">Contact Us</span>
    </nav>
    <h1 class="abs">Unlock Your<br>Financial Potential<br>with <b>K</b>estrel</h1>
    <p class="lead abs">Orci tortor euismod lectus magna justo turpis. Facilisis id non egestas lectus mi tempor convallis risus. Morbi netus donec ac at in blandit arcu.</p>
    <a class="btn abs"><span>Get a Free Consultation</span><i><svg width="12" height="10" viewBox="0 0 12 10"><path d="M1 5h9M6 1l4 4-4 4" stroke="#fff" stroke-width="1.5" fill="none"/></svg></i></a>
    <div class="service-tiles abs">
      <div class="tile">
        <svg width="30" height="30" viewBox="0 0 30 30"><path d="M5 16l10-9 10 9M8 14v11h14V14" stroke="#fff" stroke-width="1.6" fill="none"/></svg>
        <h3>Housing Loans</h3><p>Orci tortor euismod lectus magna justo turpis. Facilisis id non egestas lectus.</p>
      </div>
      <div class="tile">
        <svg width="30" height="30" viewBox="0 0 30 30"><circle cx="15" cy="15" r="11" stroke="#fff" stroke-width="1.6" fill="none"/><path d="M15 9v12M12 12h5a2 2 0 010 4h-4a2 2 0 000 4h5" stroke="#fff" stroke-width="1.4" fill="none"/></svg>
        <h3>Refinancing, Business</h3><p>Orci tortor euismod lectus magna justo turpis. Facilisis id non egestas lectus.</p>
      </div>
      <div class="tile">
        <svg width="30" height="30" viewBox="0 0 30 30"><path d="M4 24h22M8 24V14l7-5 7 5v10M13 24v-6h4v6" stroke="#fff" stroke-width="1.6" fill="none"/></svg>
        <h3>Agriculture Loans</h3><p>Orci tortor euismod lectus magna justo turpis. Facilisis id non egestas lectus.</p>
      </div>
    </div>
  </section>

  <!-- About -->
  <section class="about">
    <div class="label abs about-label">About Us</div>
    <h2 class="h2 abs">Trusted Mortgage &amp; Asset Finance<br>Experts with a Passion for Your Success</h2>
    <div class="about-copy abs body-text">
      <p>Pharetra amet nisl pulvinar amet. Pellentesque elit massa at ultrices urna nulla nisl pretium. Suspendisse orci odio posuere mauris pellentesque.</p>
      <p>Eget venenatis ac nisl. Neque mattis interdum vel ultrices dignissim nunc a aliquet morbi. Orci tortor euismod lectus magna justo turpis. Facilisis id non egestas lectus mi tempor convallis risus. Morbi netus donec ac at in blandit arcu. Id a nec facilisis scelerisque.</p>
      <ul class="bullets"><li>Pharetra amet nisl pulvinar amet.</li><li>Pharetra amet nisl pulvinar amet.</li><li>Pharetra amet nisl pulvinar amet.</li><li>Pharetra amet nisl pulvinar amet.</li></ul>
    </div>
    <a class="btn abs"><span>Learn More About</span><i><svg width="12" height="10" viewBox="0 0 12 10"><path d="M1 5h9M6 1l4 4-4 4" stroke="#fff" stroke-width="1.5" fill="none"/></svg></i></a>
    <div class="about-photo abs" role="img" aria-label="Two advisers reviewing work at a computer in a bright office"></div>
    <div class="about-photo-small abs" role="img" aria-label="Hands reviewing financial charts on paper"></div>
  </section>

  <!-- Services -->
  <section class="services abs">
    <div class="label abs">Our Services</div>
    <h2 class="h2 abs">Tailored Financial<br>Solutions for Every Need</h2>
    <p class="intro body-text abs">Pharetra amet nisl pulvinar amet. Pellentesque elit massa at ultrices urna nulla nisl pretium. Suspendisse orci odio posuere mauris pellentesque.</p>
    <div class="svc-cards abs">
      <div class="svc">
        <div class="img" role="img" aria-label="Smiling woman holding a small model house" style="background:linear-gradient(180deg,#dfe2e6 0%,#9aa6bb 45%,#2d62c4 80%,#2358bd)"></div>
        <div class="txt"><h3>Home Loans &amp;<br>Mortgages</h3><p>Pharetra amet nisl pulvinar amet. Pellentesque elit massa at ultrices urna nulla nisl pretium. Suspendisse orci odio posuere mauris pellentesque.</p>
        <a class="btn"><span>Get Started</span><i><svg width="12" height="10" viewBox="0 0 12 10"><path d="M1 5h9M6 1l4 4-4 4" stroke="#fff" stroke-width="1.5" fill="none"/></svg></i></a></div>
      </div>
      <div class="svc">
        <div class="img" role="img" aria-label="Businessman signing papers beside a laptop at sunset" style="background:linear-gradient(180deg,#9aa3b0 0%,#5b6c88 40%,#2d5fc0 78%,#2358bd)"></div>
        <div class="txt"><h3>Business<br>Finance</h3><p>Pharetra amet nisl pulvinar amet. Pellentesque elit massa at ultrices urna nulla nisl pretium. Suspendisse orci odio posuere mauris pellentesque.</p></div>
      </div>
      <div class="svc">
        <div class="img" role="img" aria-label="Hand writing on financial documents with a calculator" style="background:linear-gradient(180deg,#d7dbe3 0%,#8f9cb4 40%,#2d5fc0 78%,#2358bd)"></div>
        <div class="txt"><h3>Asset<br>Finance</h3><p>Pharetra amet nisl pulvinar amet. Pellentesque elit massa at ultrices urna nulla nisl pretium. Suspendisse orci odio posuere mauris pellentesque.</p></div>
      </div>
    </div>
    <div class="progress abs"><span>01/06</span><span class="bar"></span>
      <span class="circle" style="background:#fff"><svg width="14" height="10" viewBox="0 0 14 10"><path d="M13 5H2M6 1L2 5l4 4" stroke="#0b1a3b" stroke-width="1.5" fill="none"/></svg></span>
      <span class="circle" style="background:var(--blue-bright)"><svg width="14" height="10" viewBox="0 0 14 10"><path d="M1 5h11M8 1l4 4-4 4" stroke="#fff" stroke-width="1.5" fill="none"/></svg></span>
    </div>
  </section>

  <!-- Why us -->
  <section class="why">
    <div class="label abs">Why Us</div>
    <h2 class="h2 abs">Why Australians Trust<br>Kestrel for Finance<br>Solution</h2>
    <p class="body-text abs">Pharetra amet nisl pulvinar amet. Pellentesque elit massa at ultrices urna nulla nisl pretium. Suspendisse orci odio posuere mauris pellentesque.</p>
    <a class="btn abs"><span>Contact Us</span><i><svg width="12" height="10" viewBox="0 0 12 10"><path d="M1 5h9M6 1l4 4-4 4" stroke="#fff" stroke-width="1.5" fill="none"/></svg></i></a>
    <div class="why-photo abs" role="img" aria-label="Advisers pointing at a loan document with a calculator"></div>
    <svg class="donut abs" width="300" height="300" viewBox="0 0 300 300">
      <circle cx="150" cy="150" r="142" fill="#fff" stroke="#dfe6f3" stroke-width="2"/>
      <g transform="rotate(-90 150 150)" fill="none" stroke-width="42">
        <circle cx="150" cy="150" r="100" stroke="#1a5fb4" stroke-dasharray="308 628"/>
        <circle cx="150" cy="150" r="100" stroke="#cfdcf5" stroke-dasharray="132 628" stroke-dashoffset="-308"/>
        <circle cx="150" cy="150" r="100" stroke="#0b1a3b" stroke-dasharray="188 628" stroke-dashoffset="-440"/>
      </g>
      <circle cx="150" cy="150" r="66" fill="#fff"/>
    </svg>
    <div class="stat-note abs" style="left:530px;top:2520px;text-align:right"><b>30%</b>Access to<br>multiple lenders</div>
    <div class="stat-note abs" style="left:890px;top:2648px"><b>49%</b>Fast approvals &amp;<br>seamless process</div>
    <div class="stat-note abs" style="left:670px;top:2732px"><b>21%</b>Competitive rates<br>&amp; flexible terms</div>
  </section>

  <!-- Reviews -->
  <section class="reviews abs">
    <div class="label abs">Reviews</div>
    <h2 class="h2 abs">Customer Stories</h2>
    <div class="stars abs">★★★★★</div>
    <p class="quote abs">eget venenatis ac nisl. Neque mattis interdum vel ultrices dignissim nunc a aliquet morbi. Orci tortor euismod lectus magna justo turpis. Facilisis id non egestas lectus mi tempor convallis risus.</p>
    <div class="reviewer abs"><span class="avatar" role="img" aria-label="Customer portrait"></span><div><b>JOHN SMITH</b><small>Customer</small></div></div>
    <span class="brand mark abs">kestrel</span>
    <span class="divider abs"></span>
    <div class="stats abs">
      <div><b>100+</b><h4>HAPPY HOMEOWNERS<br>FINANCED</h4><p>Helping families achieve their<br>homeownership dreams</p></div>
      <div><b>50+</b><h4>BUSINESS LOANS<br>APPROVED</h4><p>Helping families achieve their<br>homeownership dreams</p></div>
      <div><b>20+</b><h4>LENDER<br>PARTNERSHIPS</h4><p>Strong relationships with top<br>financial institutions</p></div>
      <div><b>10+</b><h4>YEARS OF<br>EXPERIENCE</h4><p>A decade of expertise in<br>mortgage and asset finance</p></div>
    </div>
  </section>

  <!-- Contact -->
  <section class="contact">
    <div class="label abs">Get In Touch</div>
    <h2 class="h2 abs">Let’s Talk<br>Finance</h2>
    <p class="body-text abs">Pharetra amet nisl pulvinar amet. Pellentesque elit massa at ultrices urna nulla nisl pretium.</p>
    <div class="c-item abs" style="left:67px;top:3840px"><span class="circle"><svg width="16" height="16" viewBox="0 0 16 16"><path d="M3 1h3l1.5 4-2 1.2a9 9 0 004.3 4.3L11 8.5l4 1.5v3a2 2 0 01-2 2A12 12 0 011 3a2 2 0 012-2z" fill="#fff"/></svg></span><div><b>Call Us:</b><span>+(123)465-7890</span></div></div>
    <div class="c-item abs" style="left:262px;top:3840px"><span class="circle"><svg width="16" height="12" viewBox="0 0 16 12"><rect width="16" height="12" rx="2" fill="#fff"/><path d="M1 1l7 6 7-6" stroke="#1a5fb4" stroke-width="1.4" fill="none"/></svg></span><div><b>Email Us:</b><span>info@example.com</span></div></div>
    <div class="c-item abs" style="left:67px;top:3910px"><span class="circle"><svg width="14" height="18" viewBox="0 0 14 18"><path d="M7 17s6-6.5 6-10A6 6 0 001 7c0 3.5 6 10 6 10z" fill="#fff"/><circle cx="7" cy="7" r="2.2" fill="#1a5fb4"/></svg></span><div><b>Location:</b><span>ABC St, XYZ City, UK</span></div></div>
    <form class="form-card abs">
      <h3>Send Message</h3>
      <div class="row"><div class="field">First name</div><div class="field">Last Name</div></div>
      <div class="field">Email</div>
      <div class="field">Phone</div>
      <div class="field tall">Write a Message</div>
      <div class="send"><span>Send Message</span><i><svg width="12" height="10" viewBox="0 0 12 10"><path d="M1 5h9M6 1l4 4-4 4" stroke="#fff" stroke-width="1.5" fill="none"/></svg></i></div>
      <small>Mattis pellentesque consectetur elit laoreet mattis eget sit<br>sed. Ultrices feugiat metus.</small>
    </form>
  </section>

  <!-- Footer -->
  <footer class="footer abs"></footer>
  <div class="cta-card abs">
    <div class="label">Get In Touch</div>
    <h2 class="h2">Let’s make your<br>mortgage and finance<br>journey simple.</h2>
    <p>Pharetra amet nisl pulvinar amet. Pellentesque elit massa at ultrices urna nulla nisl pretium.</p>
    <a class="btn light"><span>Contact Us</span><i><svg width="12" height="10" viewBox="0 0 12 10"><path d="M1 5h9M6 1l4 4-4 4" stroke="#0b1a3b" stroke-width="1.5" fill="none"/></svg></i></a>
  </div>
  <span class="brand f-brand abs">kestrel</span>
  <p class="f-about abs">Orci tortor euismod lectus magna justo turpis. Facilisis id non egestas lectus mi tempor convallis risus. Morbi netus.</p>
  <div class="socials abs"><i></i><i></i><i></i><i></i></div>
  <div class="f-col abs" style="left:454px"><h4>Quick Links</h4><ul><li>Home</li><li>About Us</li><li>Services</li><li>Why Us</li><li>Reviews</li><li>Contact Us</li></ul></div>
  <div class="f-col abs" style="left:716px"><h4>Services</h4><ul><li>Home Loans &amp; Mortgages</li><li>Business Finance</li><li>Asset Finance</li></ul></div>
  <div class="f-col abs" style="left:976px"><h4>Contact Us</h4><ul><li>+(123)465-7890</li><li>info@example.com</li></ul></div>
  <div class="f-bottom abs"><span>copyright©2024 kestrel</span><span>Terms &amp; Condition . Faqs . Privacy Policy</span></div>

</div>
</body>
</html>
```